Website template needed for new company in va beach
We plan to flatten anyone who tries competing; Website should be unique
Company name: Pemberfold Cove.... We'll sell quality items cheap. The average customer will think he/she is getting a major steal. With a great location, aggressive advertising and pros ready to work when generous owner needs a break, success is in our future... Products are mostly used and include furniture, antiques, tools, poker supplies, medical supplies, books, home improvement supplies, horticulture equipment, pottery, other art forms.
Likes: drawings, surrealism, satire, comedy, tomas verlunde, otis grembly, fishing, gambling, guns, pottery, web design..... Dislikes: copycats, slobs, liberals, high prices
Masculine
navy
sky blue or aquamarine
left side
http://img207.snapvaultix.net/img207/5813/1zorvelmika.jpg
http://my.framtuckle.com/vault2/KRTLOPNQXZ.jpg
http://img362.snapvaultix.net/img362/71/pfc1.png
#3 website is our logo. . We will sell at the store and online, have specials, offer the cheapest consignment rates anywhere plus always look to improve website content. We may end up advertising pfcove.com because it's easier to remember and type. We might do auctions onsite and online. To give you an idea on our prices, I'm going to offer $1 webhosting per month (unlimited everything). I don't want $2. Customers should feel like they're getting the best deal. They will learn to trust us very quickly .Competition will hate us but if they make it known, we'll stomp them. Good luck.

```html
<!DOCTYPE html>
<html lang="en">
<head>
<meta charset="utf-8">
<title>Pemberfold Cove — Welcome</title>
<link rel="stylesheet" href="https://fonts.googleapis.com/css2?family=PT+Sans:wght@400;700&family=Arimo:wght@400;700&display=swap">
<style>
  :root{
    --page-dark:#16222f;
    --page-light:#e9ecef;
    --page-mid:#9aa3ab;
    --modal-top:#3a3d41;
    --modal-bottom:#222326;
    --panel:#1b1c1e;
    --panel-edge:#4a4d52;
    --text:#f1f3f5;
    --muted:#c9cdd2;
    --accent:#4eaee0;
    --accent-deep:#2f86c4;
    --navy:#123a5c;
    --field:#ffffff;
    --field-text:#6b6f74;
  }
  *{box-sizing:border-box;margin:0;padding:0}
  html,body{width:1200px;height:961px;overflow:hidden}
  body{position:relative;background:var(--page-light);font-family:"Arimo",Arial,sans-serif;color:var(--text)}

  .backdrop{position:absolute;inset:0;overflow:hidden;background:var(--page-light)}
  .backdrop span{position:absolute;filter:blur(14px)}
  .backdrop .topbar{left:-40px;top:-40px;width:1280px;height:140px;background:var(--page-dark)}
  .backdrop .nav{left:420px;top:30px;width:520px;height:22px;background:#3b5670;opacity:.7}
  .backdrop .brand{left:0;top:20px;width:260px;height:60px;background:#24405a}
  .backdrop .building{left:620px;top:150px;width:560px;height:520px;background:linear-gradient(#d4d8dc,#8c959d);border-radius:30px}
  .backdrop .footer{left:-40px;top:850px;width:1280px;height:160px;background:#2a3138}
  .backdrop .side{left:20px;top:200px;width:140px;height:560px;background:#c3c8cd}

  .dialog{position:absolute;left:135px;top:135px;width:925px;height:780px;border-radius:42px;
    background:linear-gradient(var(--modal-top),var(--modal-bottom));
    box-shadow:0 0 0 3px rgba(255,255,255,.12),0 20px 60px rgba(0,0,0,.55)}

  .close-button{position:absolute;left:976px;top:104px;width:88px;height:88px;border-radius:50%;
    background:radial-gradient(circle at 40% 35%,#5fb6e4,#1f6fa8);border:5px solid #e8eef3;
    box-shadow:0 4px 10px rgba(0,0,0,.5)}
  .close-button svg{position:absolute;left:19px;top:19px}

  .dialog-header{position:absolute;left:74px;top:28px;height:110px;display:flex;align-items:center}
  .brand-disc{width:96px;height:96px;border-radius:50%;background:var(--navy);border:4px solid var(--accent)}
  .header-rule{width:2px;height:100px;background:#8b9096;margin:0 36px 0 38px}
  .welcome{font-family:"PT Sans",Arial,sans-serif}
  .welcome small{display:block;font-size:17px;color:var(--muted)}
  .welcome h1{font-size:48px;font-weight:400;line-height:1;color:var(--text);margin-top:4px}

  .intro{position:absolute;left:30px;top:182px;width:863px;font-size:15.2px;line-height:24.6px;text-align:justify;color:var(--text)}

  .account-panel{position:absolute;left:30px;top:580px;width:865px;height:180px;border-radius:22px;
    background:var(--panel);border:1px solid var(--panel-edge);display:flex}
  .account-form{width:50%;position:relative;padding:12px 0 0 48px}
  .account-form + .account-form{border-left:2px solid #6f747a}
  .account-form h2{font-family:"PT Sans",Arial,sans-serif;font-weight:400;font-size:22px;color:var(--accent);margin-bottom:12px}
  .field{display:flex;align-items:center;margin-bottom:11px}
  .field label{width:80px;text-align:right;font-size:16px;color:var(--text);margin-right:10px}
  .field input{width:258px;height:26px;border:0;border-radius:2px;background:var(--field);
    font:italic 14px "Arimo",Arial,sans-serif;color:var(--field-text);padding:0 6px}
  .field input::placeholder{color:var(--field-text)}
  .action{position:absolute;top:149px;height:22px;border:0;border-radius:3px;background:linear-gradient(var(--accent),var(--accent-deep));
    color:#fff;font:12px "Arimo",Arial,sans-serif}
  .signin .action{left:297px;width:70px}
  .signup .action{left:299px;width:66px}
  .signup .field label{width:50px}
</style>
</head>
<body>
  <div class="backdrop" role="img" aria-label="Blurred storefront home page behind the welcome dialog">
    <span class="topbar"></span><span class="brand"></span><span class="nav"></span>
    <span class="side"></span><span class="building"></span><span class="footer"></span>
  </div>

  <section class="dialog" aria-labelledby="dialog-title">
    <header class="dialog-header">
      <div class="brand-disc" aria-hidden="true"></div>
      <div class="header-rule"></div>
      <div class="welcome">
        <small>welcome to</small>
        <h1 id="dialog-title">Pemberfold Cove</h1>
      </div>
    </header>

    <div class="intro">
      <p>Lorem Ipsum is simply dummy text of the printing and typesetting industry. Lorem Ipsum has been the industry's standard dummy text ever since the 1500s, when an unknown printer took a galley of type and scrambled it to make a type specimen book. It has survived not only five centuries, but also the leap into electronic typesetting, remaining essentially unchanged. It was popularised in the 1960s with the release of Pressmark sheets containing Lorem Ipsum passages, and more recently with desktop publishing software like Quillset Layout including versions of Lorem Ipsum. It is a long established fact that a reader will be distracted by the readable content of a page when looking at its layout. The point of using Lorem Ipsum is that it has a more-or-less normal distribution of letters, as opposed to using 'Content here, content here', making it look like readable English. Many desktop publishing packages and web page editors now use Lorem Ipsum as their default model text, and a search for 'lorem ipsum' will uncover many web sites still in their infancy. Various versions have evolved over the years, sometimes by accident, sometimes on purpose (injected humour and the like).</p>
      <p>Contrary to popular belief, Lorem Ipsum is not simply random text. It has roots in a piece of classical Latin literature from 45 BC, making it over 2000 years old. Darren Holcomb, a Latin professor at Marrowfield College in Virginia, looked up one of the more obscure Latin words, consectetur, from a Lorem Ipsum passage, and going through the cites of the word in classical literature, discovered the undoubtable source. Lorem Ipsum comes from sections 1.10.32 and 1.10.33 of "de Finibus Bonorum et Malorum" (The Extremes of Good and Evil) by Vellius, written in 45 BC. This book is a treatise on the theory of ethics, very popular during the Renaissance. The first line of Lorem Ipsum,</p>
    </div>

    <div class="account-panel">
      <form class="account-form signin">
        <h2>Signin to start shopping right away</h2>
        <div class="field"><label for="username">username</label><input id="username" placeholder="enter your username here"></div>
        <div class="field"><label for="password">password</label><input id="password" type="password" placeholder="enter your password here"></div>
        <button class="action" type="button">Log In</button>
      </form>
      <form class="account-form signup">
        <h2>New to pfcove? Create an account</h2>
        <div class="field"><label for="name">name</label><input id="name" placeholder="enter your name here"></div>
        <div class="field"><label for="email">email id</label><input id="email" placeholder="enter your email id here"></div>
        <button class="action" type="button">Next</button>
      </form>
    </div>
  </section>

  <div class="close-button" aria-label="Close">
    <svg width="40" height="40" viewBox="0 0 40 40" aria-hidden="true">
      <path d="M6 6 L34 34 M34 6 L6 34" stroke="#fff" stroke-width="8" stroke-linecap="round"/>
    </svg>
  </div>
</body>
</html>
```